Corvel's Auto Detailing is the company name. I will upload a picture that is something similar. However a few things will be different. I want my company name to be on it. And a picture of a nice car. As well as the packages offered. Also phone number which is 5047162283. Call or text. As far as the packages goes, I want the exact layout of the picture I uploaded. The only difference would be the prices. For full detail the price should be $149.99, engine detail is $39.99 headlight restoration is $19.99 exterior wash is $59.99 Interior is $59.99. Please make it pretty. I would like to see a copy before printing

```html
<!DOCTYPE html>
<html lang="en">
<head>
<meta charset="utf-8">
<title>Corvel's Auto Detailing – Service Menu</title>
<link href="https://fonts.googleapis.com/css2?family=Fira+Sans+Condensed:ital,wght@0,500;0,600;0,700;1,600&family=Fira+Sans+Extra+Condensed:wght@700&family=Open+Sans:ital,wght@0,800;1,700&display=swap" rel="stylesheet">
<style>
  :root{
    --stage:#e8e5e0;
    --gap:#ffffff;
    --yellow:#f7e31c;
    --red:#e11d1d;
    --ink:#151515;
    --label-bg:#ffffff;
    --full-a:#55578c; --full-b:#3b3c68;
    --int-a:#2c3150; --int-b:#1b1f36;
    --eng-a:#5a5a5e; --eng-b:#2f2f33;
    --ext-a:#2a2747; --ext-b:#16142a;
    --strip:#efefef;
  }
  *{margin:0;padding:0;box-sizing:border-box}
  html,body{width:1200px;height:900px;overflow:hidden;background:var(--stage)}
  .menu-card{position:absolute;left:80px;top:103px;width:1040px;height:694px;background:var(--gap);box-shadow:0 2px 8px rgba(0,0,0,.15)}
  .panel{position:absolute;overflow:hidden}
  .panel-photo{position:absolute;inset:0}
  .panel-full{left:0;top:0;width:585px;height:357px}
  .panel-full .panel-photo{background:radial-gradient(ellipse at 45% 75%,#6a6ca0 0%,var(--full-a) 40%,var(--full-b) 100%)}
  .panel-interior{left:593px;top:0;width:447px;height:357px}
  .panel-interior .panel-photo{background:linear-gradient(135deg,var(--int-a),var(--int-b))}
  .panel-engine{left:0;top:365px;width:534px;height:272px}
  .panel-engine .panel-photo{background:radial-gradient(ellipse at 60% 55%,#77777b 0%,var(--eng-a) 40%,var(--eng-b) 100%)}
  .panel-exterior{left:542px;top:365px;width:498px;height:329px}
  .panel-exterior .panel-photo{background:linear-gradient(160deg,var(--ext-a),var(--ext-b))}
  .abs{position:absolute}

  .brand-name{left:82px;top:10px;width:420px;text-align:center;font:700 44px/50px "Fira Sans Condensed",sans-serif;color:var(--yellow)}
  .package-label{position:absolute;background:var(--label-bg);border-radius:10px;color:var(--red);font:700 22px/1 "Fira Sans Condensed",sans-serif;display:flex;align-items:center;justify-content:center;box-shadow:0 2px 4px rgba(0,0,0,.35)}
  .package-label.caps{font-size:21px;letter-spacing:.3px}

  .service-list{position:absolute;list-style:none;color:var(--yellow);font:600 12.5px/17px "Fira Sans Condensed",sans-serif;text-transform:uppercase}
  .service-list li{position:absolute;left:0;padding-left:18px;white-space:nowrap}
  .service-list li::before{content:"";position:absolute;left:1px;top:4px;width:7px;height:7px;background:var(--red);transform:rotate(45deg)}
  .service-list.large{font-size:14.5px;line-height:21px}
  .service-list.large li{padding-left:22px}
  .service-list.large li::before{top:6px;width:8px;height:8px}
  .service-list.white{color:#fff}

  .price-box{position:absolute;background:#fff;border:2px solid var(--red);text-align:center;color:var(--ink)}
  .price-box .lead{display:block;font:italic 700 18px/1 "Open Sans",sans-serif}
  .price-box .amount{font:800 34px/1 "Open Sans",sans-serif;color:var(--red);text-shadow:1px 2px 0 #4a0a0a}
  .price-box .tax{font:italic 700 17px/1 "Open Sans",sans-serif;margin-left:6px}
  .price-box.big .lead{font-size:23px}
  .price-box.big .amount{font-size:50px}
  .price-box.big .tax{font-size:21px}

  .headline{left:34px;top:522px;color:var(--yellow);font:700 60px/50px "Fira Sans Extra Condensed",sans-serif}
  .headline span{display:block}
  .headline .line-two{font-size:58px}

  .footer-strip{left:0;top:637px;width:534px;height:57px;background:var(--strip);text-align:center}
  .footer-strip .notice{display:block;margin-top:8px;color:var(--red);font:700 18px/20px "Fira Sans Condensed",sans-serif}
  .footer-strip .contact{display:block;font:600 13.5px/18px "Fira Sans Condensed",sans-serif;color:var(--ink)}
  .footer-strip .contact b{color:var(--red);font-weight:700;font-size:15px}
</style>
</head>
<body>
<main class="menu-card">

  <section class="panel panel-full">
    <div class="panel-photo" role="img" aria-label="Photo of a detailed sports car front, tinted purple"></div>
    <h1 class="abs brand-name">Corvel's Auto Detailing</h1>
    <h2 class="package-label" style="left:30px;top:67px;width:110px;height:30px">Full Detail</h2>
    <ul class="service-list" style="left:36px;top:103px">
      <li style="top:0">Wash car &amp; dry with<br>microfiber towels</li>
      <li style="top:42px">Clean wheels &amp; wheels<br>wells</li>
      <li style="top:84px">Vacuum carpets &amp; mats</li>
      <li style="top:112px">Vacuum interior &amp;<br>trunk</li>
      <li style="top:153px">Apply polish for shine<br>&amp; to remove minor<br>scratches</li>
    </ul>
    <ul class="service-list" style="left:224px;top:103px">
      <li style="top:0">Shampoo carpets, floor<br>mats, seats</li>
      <li style="top:42px">Clean all windows &amp;<br>mirrors</li>
      <li style="top:84px">Wipe door jams</li>
      <li style="top:113px">Apply conditioner to<br>leather seats</li>
    </ul>
    <ul class="service-list" style="left:412px;top:103px">
      <li style="top:0">Apply premium wax to<br>protect the clear coat</li>
      <li style="top:42px">Deep clean upholstery<br>&amp; leather</li>
      <li style="top:84px">Apply tire dressing</li>
      <li style="top:113px">Clean all windows<br>&amp; mirrors</li>
    </ul>
    <div class="price-box" style="left:214px;top:260px;width:213px;height:80px;padding-top:10px">
      <span class="lead">Starting At</span>
      <span class="amount">$149.99</span><span class="tax">+ Tax</span>
    </div>
  </section>

  <section class="panel panel-interior">
    <div class="panel-photo" role="img" aria-label="Photo of a dark car interior seen through the open door"></div>
    <h2 class="package-label caps" style="left:23px;top:29px;width:171px;height:40px">INTERIOR DETAIL</h2>
    <ul class="service-list large" style="left:39px;top:82px">
      <li style="top:0">Wash car &amp; dry with<br>microfiber towels</li>
      <li style="top:52px">Vacuum interior<br>&amp; trunk</li>
      <li style="top:102px">Shampoo carpets,<br>floor mats,</li>
    </ul>
    <ul class="service-list large" style="left:244px;top:82px">
      <li style="top:0">Seats deep clean<br>upholstery &amp; leather</li>
      <li style="top:52px">Apply conditioner<br>to leather seats</li>
      <li style="top:102px">Clean all windows<br>&amp; mirrors</li>
    </ul>
    <div class="price-box big" style="left:64px;top:238px;width:271px;height:104px;padding-top:13px">
      <span class="lead">Starting At</span>
      <span class="amount">$59.99</span><span class="tax">+ Tax</span>
    </div>
  </section>

  <section class="panel panel-engine">
    <div class="panel-photo" role="img" aria-label="Photo of a clean car engine bay in grey tones"></div>
    <h2 class="package-label" style="left:30px;top:23px;width:179px;height:39px;font-size:24px">Engine Detail</h2>
    <ul class="service-list white" style="left:42px;top:78px;font-size:13px;line-height:16px">
      <li style="top:0">Degrease engine, apply dressing<br>to engine, clean hood<br>compartment</li>
    </ul>
    <div class="price-box" style="left:274px;top:48px;width:226px;height:86px;padding-top:10px">
      <span class="lead">Starting At</span>
      <span class="amount" style="font-size:38px">$39.99</span><span class="tax" style="margin-left:14px">+ Tax</span>
    </div>
    <div class="price-box" style="left:324px;top:170px;width:170px;height:63px;padding-top:11px">
      <span class="amount" style="font-size:38px">$19.99</span>
    </div>
  </section>

  <h2 class="abs headline"><span>HEADLIGHT</span><span class="line-two">Restoration</span></h2>

  <footer class="abs footer-strip">
    <span class="notice">ADDITIONAL CHARGES APPLY FOR LARGER VEHICLES</span>
    <span class="contact">Call Us: <b>504-716-2283</b>, Call or text for any package</span>
  </footer>

  <section class="panel panel-exterior">
    <div class="panel-photo" role="img" aria-label="Photo of a glossy dark sedan in a garage"></div>
    <h2 class="package-label caps" style="left:22px;top:27px;width:187px;height:40px">EXTERIOR DETAIL</h2>
    <ul class="service-list" style="left:35px;top:86px">
      <li style="top:0">Wash car &amp; dry with<br>microfiber towels</li>
      <li style="top:42px">Clean all windows<br>and mirrors</li>
      <li style="top:85px">Apply polish for<br>shine &amp; to remove<br>minor scratches</li>
      <li style="top:147px">Apply premium wax<br>to protect clear coat</li>
    </ul>
    <ul class="service-list" style="left:192px;top:86px">
      <li style="top:0">Clean wheels &amp; wheel<br>wells</li>
      <li style="top:42px">Vacuum carpets<br>&amp; mats</li>
    </ul>
    <ul class="service-list" style="left:358px;top:86px">
      <li style="top:0">Apply tire dressing</li>
      <li style="top:42px">Wipe door jams</li>
    </ul>
    <div class="price-box big" style="left:202px;top:184px;width:250px;height:96px;padding-top:10px">
      <span class="lead" style="font-size:21px">Starting At</span>
      <span class="amount" style="font-size:46px">$59.99</span><span class="tax">+ Tax</span>
    </div>
  </section>

</main>
</body>
</html>
```